Moving Invitation for VIP Dinner at Zorava Lounge (Video/GIF)

Project Description:
I am seeking a creative designer to produce a moving invitation (video or GIF) for our upcoming VIP dinner at Zorava Lounge during the KTRL conference. The invite should capture the luxurious, exotic, and Moroccan-inspired vibe of the venue, while maintaining a professional, high-end feel. I like the idea of a Sahara desert background with the sand moving - or something like that. Open to all creative ideas though!
Key Requirements:
Theme: Moroccan/Arabic luxury with elegant animations that reflect the atmosphere of Zorava Lounge or of a Moroccan desert.
Content: Event name (NOR-Q Dinner), date (July 18th), time (8pm-10pm EST), location (Zorava Lounge), and RSVP details (contact Delphine Ashcott @ dashcott@plumora.com)
Branding: Prominently feature the TEL RUNO KB and PLUMORA logos (I will provide high-resolution files)
Tone: Luxurious, exclusive, and sophisticated, with a touch of mystique
Format: High-quality MP4, GIF, and social media-friendly formats (Instagram story, LinkedIn post)
Deliverables:
Final moving invite in MP4 and GIF formats
Editable project file (After Effects, Premiere, or similar) for future updates
Timeline: First draft within 2-3 days.
Company hosting the dinner: https://telrunokb.com/
Conference being hosted at: https://ktrlspine.com/miami2025/

Target Market(s)
Physicians

```html
<!DOCTYPE html>
<html lang="en">
<head>
<meta charset="utf-8">
<title>NOR-Q Dinner Invitation</title>
<link href="https://fonts.googleapis.com/css2?family=Cinzel:wght@400;500&display=swap" rel="stylesheet">
<style>
  :root {
    --royal-purple: #44106f;
    --purple-light: #4e167f;
    --purple-dark: #3a0c62;
    --deep-plum: #22073f;
    --gold: #e2b20c;
    --gold-light: #f3cf4a;
    --gold-dark: #c8930a;
    --white: #ffffff;
  }
  html, body {
    margin: 0;
    padding: 0;
    overflow: hidden;
    background: var(--royal-purple);
  }
  .invite {
    position: relative;
    width: 675px;
    height: 1200px;
    overflow: hidden;
    background: var(--royal-purple);
    font-family: "Cinzel", serif;
    color: var(--gold);
  }
  .damask-backdrop {
    position: absolute;
    inset: 0;
    background:
      radial-gradient(ellipse at 50% 45%, var(--purple-light) 0%, var(--royal-purple) 55%, var(--purple-dark) 100%);
  }
  .invite__art {
    position: absolute;
    inset: 0;
    width: 675px;
    height: 1200px;
  }
  .gold-text {
    background: linear-gradient(180deg, var(--gold-light) 0%, var(--gold) 55%, var(--gold-dark) 100%);
    -webkit-background-clip: text;
    background-clip: text;
    color: transparent;
  }
  .event-title {
    position: absolute;
    top: 186px;
    left: 0;
    width: 100%;
    margin: 0;
    text-align: center;
    font-size: 60px;
    font-weight: 400;
    line-height: 1;
    letter-spacing: 0.5px;
  }
  .event-details {
    position: absolute;
    top: 527px;
    left: 0;
    width: 100%;
    margin: 0;
    text-align: center;
    font-size: 37px;
    line-height: 45px;
  }
  .event-details__line { display: block; }
  .event-details__venue {
    display: flex;
    justify-content: center;
    align-items: center;
    gap: 12px;
  }
  .venue-pin {
    width: 14px;
    height: 20px;
    flex: none;
    margin-top: 4px;
  }
  .venue-name {
    background: linear-gradient(180deg, var(--gold-light) 0%, var(--gold) 55%, var(--gold-dark) 100%);
    -webkit-background-clip: text;
    background-clip: text;
    color: transparent;
  }
  .rsvp {
    position: absolute;
    top: 891px;
    left: 0;
    width: 100%;
    text-align: center;
    font-size: 23px;
    line-height: 29px;
    color: var(--gold);
  }
  .rsvp__line { display: block; }
  .brand-row {
    position: absolute;
    top: 983px;
    left: 0;
    width: 100%;
    display: flex;
    justify-content: center;
    gap: 22px;
    font-size: 25px;
    font-weight: 500;
    line-height: 1;
    color: var(--white);
  }
</style>
</head>
<body>
<main class="invite">
  <div class="damask-backdrop" role="img" aria-label="Purple damask swirl pattern background"></div>

  <svg class="invite__art" viewBox="0 0 1080 1920">
    <rect class="frame-outer" x="77" y="90" width="926" height="1740" fill="none" stroke="var(--gold)" stroke-width="5"/>
    <rect class="frame-inner" x="102" y="115" width="876" height="1690" fill="none" stroke="var(--gold)" stroke-width="4"/>

    <path class="lantern-panel"
      d="M540 530 C545 610 590 660 640 695 L740 695 L740 778
         C830 830 862 900 862 960 C862 1020 830 1090 740 1142
         L740 1225 L640 1225 C590 1260 545 1310 540 1390
         C535 1310 490 1260 440 1225 L340 1225 L340 1142
         C250 1090 217 1020 217 960 C217 900 250 830 340 778
         L340 695 L440 695 C490 660 535 610 540 530 Z"
      fill="var(--deep-plum)" stroke="var(--gold)" stroke-width="2.5"/>

    <g class="rail" fill="var(--gold)">
      <rect x="190" y="815" width="700" height="4"/>
      <rect x="178" y="807" width="25" height="20"/>
      <rect x="877" y="807" width="25" height="20"/>
      <rect x="190" y="1100" width="700" height="4"/>
      <rect x="178" y="1092" width="25" height="20"/>
      <rect x="877" y="1092" width="25" height="20"/>
    </g>

    <rect x="500" y="660" width="80" height="100" rx="30" fill="var(--gold)" opacity="0.3" role="img" aria-label="Gold floral ornament at top of lantern"/>
    <rect x="500" y="1160" width="80" height="100" rx="30" fill="var(--gold)" opacity="0.3" role="img" aria-label="Gold floral ornament at bottom of lantern"/>

    <g class="sparkle-accents" fill="var(--gold)" opacity="0.35">
      <circle cx="304" cy="752" r="18" role="img" aria-label="Gold sparkle accent"/>
      <circle cx="776" cy="752" r="18" role="img" aria-label="Gold sparkle accent"/>
      <circle cx="304" cy="1166" r="18" role="img" aria-label="Gold sparkle accent"/>
      <circle cx="776" cy="1166" r="18" role="img" aria-label="Gold sparkle accent"/>
    </g>

    <rect class="divider" x="252" y="1537" width="576" height="2" fill="var(--gold)"/>
  </svg>

  <h1 class="event-title gold-text">NOR-Q Dinner</h1>

  <p class="event-details">
    <span class="event-details__line gold-text">July 18th</span>
    <span class="event-details__line gold-text">8pm-10pm EST</span>
    <span class="event-details__line event-details__venue">
      <svg class="venue-pin" viewBox="0 0 14 20" aria-hidden="true">
        <path d="M7 0 a7 7 0 0 1 7 7 c0 6 -7 13 -7 13 c0 0 -7 -7 -7 -13 a7 7 0 0 1 7 -7 Z" fill="var(--gold)"/>
        <circle cx="7" cy="7" r="3" fill="var(--deep-plum)"/>
      </svg>
      <span class="venue-name">Zorava Lounge</span>
    </span>
  </p>

  <div class="rsvp">
    <span class="rsvp__line">Delphine Ashcott</span>
    <span class="rsvp__line">dashcott@plumora.com</span>
  </div>

  <div class="brand-row">
    <span class="brand-name">TEL RUNO KB</span>
    <span class="brand-name">PLUMORA</span>
  </div>
</main>
</body>
</html>
```